Business Card Design Project

Corvexa logo will be provided after
Front

Bram Oskarsen- Construction Manager

Ph: (61) 07 53182907
boskarsen@corvexa.com.au
PO Box 83 Kelbarra 4529

Back
Corvexa
EPCM

Oil - Gas - Mining

Industry/Entity Type

Business

Font styles to use
Sans Serif

Colors
faa54b

Requirements
Must have
• White Back Ground

```html
<!DOCTYPE html>
<html lang="en">
<head>
<meta charset="UTF-8">
<title>Corvexa EPCM — Business Card</title>
<link rel="stylesheet" href="https://fonts.googleapis.com/css2?family=Lexend:wght@300;400;600;700&display=swap">
<style>
  :root {
    --brand-orange: #eb9545;
    --card-white: #f7f7f5;
    --backdrop: #232323;
    --text-on-orange: #ffffff;
    --card-w: 500px;
    --card-h: 305px;
  }
  * { box-sizing: border-box; margin: 0; padding: 0; }
  html, body {
    width: 1200px;
    height: 800px;
    overflow: hidden;
  }
  body {
    background: var(--backdrop);
    font-family: "Lexend", "Helvetica Neue", Arial, sans-serif;
    display: flex;
    align-items: center;
    justify-content: center;
    gap: 60px;
  }
  .card {
    width: var(--card-w);
    height: var(--card-h);
    border-radius: 3px;
    box-shadow: 0 10px 28px rgba(0, 0, 0, 0.45);
    display: flex;
    flex-direction: column;
    align-items: center;
    justify-content: center;
    text-align: center;
  }

  /* Front: contact side */
  .card--front {
    background: var(--card-white);
    color: var(--brand-orange);
  }
  .contact-name {
    font-weight: 600;
    font-size: 25px;
    letter-spacing: 0.3px;
  }
  .contact-role {
    font-weight: 300;
    font-size: 18px;
    margin-top: 6px;
    letter-spacing: 0.4px;
  }
  .contact-details {
    list-style: none;
    margin-top: 38px;
    font-weight: 300;
    font-size: 18px;
    line-height: 1.45;
    letter-spacing: 0.4px;
  }

  /* Back: brand side */
  .card--back {
    background: var(--brand-orange);
    color: var(--text-on-orange);
  }
  .brand-mark {
    width: 34px;
    height: 34px;
    border-radius: 50%;
    background: var(--text-on-orange);
    margin-bottom: 18px;
  }
  .brand-name {
    font-weight: 700;
    font-size: 40px;
    letter-spacing: 2px;
    line-height: 1;
  }
  .brand-division {
    font-weight: 400;
    font-size: 26px;
    letter-spacing: 3px;
    margin-top: 8px;
  }
</style>
</head>
<body>
  <section class="card card--front" aria-label="Business card front">
    <h1 class="contact-name">Bram Oskarsen</h1>
    <p class="contact-role">Construction Manager</p>
    <ul class="contact-details">
      <li>Ph: (61) 07 53182907</li>
      <li>boskarsen@corvexa.com.au</li>
      <li>PO Box 83 Kelbarra 4529</li>
    </ul>
  </section>

  <section class="card card--back" aria-label="Business card back">
    <span class="brand-mark" aria-hidden="true"></span>
    <p class="brand-name">CORVEXA</p>
    <p class="brand-division">EPCM</p>
  </section>
</body>
</html>
```